Urban Health Evangelism Bifold Brochure

We need a brochure designed to advertise upcoming youth health evangelism training in the New York City urban areas. The brochure will target young people and Pastors in local churches who would like to get their young members involved.

COPY 1
“Rise”…..Rise Like a Gideon

Are you a youth or young at heart and want to live and work for God but your not sure how? You have the heart of a missionary but not the means? Wanna make a big difference right here right now in the lives of others?

Then you are the one God is calling to be apart of KR27’s Urban Health Evangelism Training, “Rise”, as in Rise Like a Gideon. Consisting of Medical Missionary, Canvassing and Bible Work Training. You will learn:

• How to help people in reversing lifestyle diseases- Diabetes, Heart Disease, Hypertension etc.
• How to use Health to bring Souls into the kingdom
• How to do both of the above while earning an income and immediately walk away with earnings as you leave the training.

Wanna make a difference right here, right now, then sign up today and become equip, empowered and enriched.

Pastors:

How would you like to see your youth transformed into preachers, teachers and health educators bringing optimal health in the reach of their communities and their church?

VelmoraWell has teamed up with the PTA for KR27 in Urban Health Evangelism. A systematic approach that offers outreach opportunity for the young and young at heart, that promises to mobilization your youth bringing them to the frontlines of evangelism for KR27 and beyond.

COPY 2
Youth Leaders are able:
• To engage the youth in evangelism giving them real participation in the commission of our church to go and teach all.
• Give outreach opportunity while building an income for the youth department and individual youth.
There are not many programs that will educate equip and financially empower but this is one.

The Youth:

You will play an important role in KR27 by tilling the soil of souls through cold meet consultations and WOW presentations at various institutions and churches. Showing people first how they can experience optimal health through lifestyle changes so simple even a child can teach them, all the while generating interest for the church and income for yourself.
You will discover like Daniel and the three Hebrew boys the Mental, Physical and Moral Advantage.

Here are some of the courses offered:

Self Support Work: A workman is worthy of his wages. This class shows how to utilize the skills you acquire in the training to see a monetary return for years to come. You will gain practical experience in the field and possibly walk away with a profit by the end of the training. I have never attended a training where you can walk away with money.

God’s Healing Program:
"There are many ways of practicing the healing art but only one that God approves." -MH118.4 This class is a look at God’s simple approach to healing and helps one to know the difference between the false and true healing practices.
Disease and Treatment:
A comprehensive look at the causes of various lifestyle diseases, diabetes, hypertension, heart disease and more how to reverse them using God’s simple healing approach. Very scientific
The 8-Laws of Health:
Fundamental to any medical missionary training are the 8 guidelines that help to define and reverse diseases.

COPY 3
Pampering Party:
Massage/Hydrotherapy
An introduction to Massage Therapy and Water treatments that help with lowering blood pressure, management of arthritic pain and more.
Cooking Demo:
This cooking demo is like no other. We know that as a total vegetarian one can enjoy food that is um um good, but just how good? We will invite some of our talented local chefs to lead out in a challenge to see how good is good in the vegetarian world. Meanwhile, you learn how to prepare these meals yourself so that you can go and teach others.
So Fresh and So Clean: It’s God’s will for you to look great.
What can I wear? I’m not a nun but I want to carry myself as an attractive youthful Christian. If you have ever felt anything close to this, you’ll love our class on fashion. We will look at what the bible says on what to wear. You get to attend and participate in our fashion show of classy beautiful looks for the seasons that are easy on the eyes and the pockets. Also learn about natural skin, and hair care. When we are through you’ll be so fresh you would be able to stand yourself.

Time: You set the time

Location: Your Church

Cost: $350 covers: course fee and books, DVD’s, additional material

COPY 4
Application:

Name: ________________________________________________________________________________________
Address: _____________________________________________________________________________________
Email: ____________________________________________
Phone: ___________________________________________
Church Affiliation: ______________________________
Age: ______________________________________________

The young and young at heart, also Pastors in local Ninth-hour Covenantist churches

Training

• The included logos must be included. COPY can be manipulated to fit design, but message intent must remain intact. Logos can be placed on last page/same page as program application form (COPY 4)

```html
<!DOCTYPE html>
<html lang="en">
<head>
<meta charset="utf-8">
<title>Rise Like a Gideon – Urban Health Evangelism Training</title>
<link rel="stylesheet" href="https://fonts.googleapis.com/css2?family=Arimo:wght@400;700&family=Major+Mono+Display&display=swap">
<style>
  :root {
    --sky: #1aa3e8;
    --sky-soft: #7fd0f5;
    --paper: #ffffff;
    --ink: #1b1f5e;
    --ink-soft: #2a2f6e;
    --orange: #f08a24;
    --rule: #1b1f5e;
    --body: "Arimo", Arial, sans-serif;
    --display: "Major Mono Display", monospace;
  }
  * { box-sizing: border-box; margin: 0; padding: 0; }
  html, body { width: 1200px; height: 426px; overflow: hidden; background: var(--paper); }
  .brochure { display: flex; width: 1200px; height: 426px; font-family: var(--body); color: var(--ink); }
  .panel { position: relative; width: 300px; height: 426px; padding: 12px 14px; overflow: hidden; }

  .panel--intro { background: linear-gradient(180deg, var(--paper) 0%, var(--paper) 30%, var(--sky-soft) 70%, var(--sky) 100%); }
  .panel--program { background: linear-gradient(180deg, var(--sky) 0%, var(--paper) 18%, var(--paper) 70%, var(--sky) 100%); border-left: 4px solid var(--sky); }
  .panel--pamper { background: linear-gradient(180deg, var(--paper) 0%, var(--paper) 55%, var(--sky) 100%); }
  .panel--apply { background: linear-gradient(180deg, var(--sky) 0%, var(--sky-soft) 25%, var(--paper) 50%, var(--paper) 70%, var(--sky) 100%); border-left: 3px solid var(--sky); }

  .title { font-family: var(--display); color: var(--orange); text-align: center; font-size: 17px; line-height: 1.15; letter-spacing: 1px; }
  .title--boxed { display: block; width: 170px; margin: 30px auto 22px; padding: 5px 4px; border: 2px dotted var(--orange); }
  .title--apply { margin: 60px auto 0; font-size: 20px; }

  .lead { font-weight: 700; font-size: 8.3px; line-height: 1.3; color: var(--ink); }
  .lead em { font-style: normal; color: var(--orange); }
  .lead--left { width: 150px; margin: 14px 0 0 10px; }
  .lead--right { width: 140px; margin: 8px 0 0 120px; text-align: center; }
  .lead--mid { text-align: center; margin: 8px 0 0; }
  .lead u { color: var(--orange); }
  .small { font-size: 5.4px; line-height: 1.3; }
  .strong { font-weight: 700; }
  .list { list-style: none; font-size: 5.4px; line-height: 1.3; margin-top: 3px; }
  .dots { text-align: center; font-size: 8px; letter-spacing: 1px; line-height: 0.8; margin: 4px 0; color: var(--ink); }
  .columns { display: flex; gap: 8px; font-size: 5.4px; line-height: 1.35; }
  .columns p { flex: 1; }

  .center { text-align: center; }
  .head { font-weight: 700; text-align: center; font-size: 7.5px; margin-top: 6px; }
  .head--u { text-decoration: underline; font-size: 8.5px; }
  .section-title { font-family: var(--display); color: var(--orange); text-align: center; font-size: 10px; margin: 8px 0 4px; }
  .body { font-size: 5.4px; line-height: 1.35; margin-top: 3px; }
  .slogan { font-weight: 700; color: var(--orange); text-align: center; font-size: 7.3px; margin: 8px 0 5px; }
  .detail { font-size: 5.4px; line-height: 1.35; margin-top: 4px; }
  .detail b { font-size: 6.5px; }

  .form { margin: 48px 0 0 10px; width: 270px; border: 1.5px dotted var(--ink); background: var(--paper); padding: 6px 10px 14px; }
  .form h2 { font-size: 11px; text-align: center; margin-bottom: 6px; }
  .field { display: flex; font-size: 6px; line-height: 1; margin-top: 4px; }
  .field span { flex: 1; border-bottom: 0.8px solid var(--ink); margin-left: 2px; }
  .field--gap { margin-top: 8px; }

  .partners { position: absolute; left: 20px; right: 10px; bottom: 36px; display: flex; align-items: center; justify-content: space-between; }
  .partner { display: flex; align-items: center; gap: 3px; font-size: 7px; font-weight: 700; color: var(--ink); }
  .partner svg { display: block; }
</style>
</head>
<body>
<main class="brochure">

  <section class="panel panel--intro">
    <h1 class="title">“rise”…<br>rise like a gideon</h1>
    <p class="lead lead--left">Are you a <em>youth</em> or young at heart and want to live and work for God but your not sure how?</p>
    <p class="lead lead--right">You have the <em>heart</em> of a missionary but not the means?</p>
    <p class="lead lead--left" style="margin-top:6px">Wanna <em>make a big difference</em> right here right now in the lives of others?</p>
    <p class="lead lead--mid">Then you are the one God is calling to be a part of<br><u>KR27’s Urban Health Evangelism Training</u>,<br>“Rise”, as in Rise Like a Gideon.</p>
    <p class="small strong" style="margin-top:6px">Consisting of Medical Missionary, Canvassing and Bible Work Training.</p>
    <p class="small strong" style="margin-top:5px">You will learn:</p>
    <ul class="list">
      <li>• How to help people in reversing lifestyle diseases- Diabetes, Heart Disease, Hypertension etc.</li>
      <li>• How to use Health to bring Souls into the kingdom</li>
      <li>• How to do both of the above while earning an income and immediately walk away with earnings as you leave the training.</li>
    </ul>
    <p class="dots">. . . . . . . . . . .</p>
    <p class="lead center" style="font-size:7.4px"><u>Wanna make a difference right here, right now, then sign up today and become equip, empowered and enriched.</u></p>
    <p class="dots">. . . . . . . . . . .</p>
    <p class="small strong center">Pastors:</p>
    <div class="columns" style="margin-top:4px">
      <p>How would you like to see your youth transformed into preachers, teachers and health educators bringing optimal health in the reach of their communities and their church? VelmoraWell has teamed up with the PTA for KR27 in Urban Health</p>
      <p>Evangelism. A systematic approach that offers outreach opportunity for the young and young at heart, that promises to mobilization your youth bringing them to the frontlines of evangelism for KR27 and beyond.</p>
    </div>
  </section>

  <section class="panel panel--program">
    <p class="head">Youth Leaders are able:</p>
    <p class="body center strong">1—<br><span style="font-weight:400">To engage the youth in evangelism giving them real participation in the commission of our church to go and teach all.</span><br>2—<br><span style="font-weight:400">Give outreach opportunity while building an income for the youth department and individual youth.</span></p>
    <p class="head" style="font-size:7px">There are not many programs that will educate equip and financially empower but this is one.</p>
    <p class="head head--u" style="margin-top:10px">The Youth</p>
    <p class="body">You will play an important role in KR27 by tilling the soil of souls through cold meet consultations and WOW presentations at various institutions and churches. Showing people first how they can experience optimal health through lifestyle changes so simple even a child can teach them, all the while generating interest for the church and income for yourself.<br>You will discover like Daniel and the three Hebrew boys the Mental, Physical and Moral Advantage.</p>
    <h2 class="section-title">some of the course offered</h2>
    <p class="head">Self Support Work</p>
    <p class="body">A workman is worthy of his wages. This class shows how to utilize the skills you acquire in the training to see a monetary return for years to come. You will gain practical experience in the field and possibly walk away with a profit by the end of the training. I have never attended a training where you can walk away with money.</p>
    <p class="head">God’s Healing Program</p>
    <p class="body">“There are many ways of practicing the healing art but only one that God approves.” -MH118.4 This class is a look at God’s simple approach to healing and helps one to know the difference between the false and true healing practices.</p>
    <p class="head">Disease and Treatment</p>
    <p class="body">A comprehensive look at the causes of various lifestyle diseases, diabetes, hypertension, heart disease and more how to reverse them using God’s simple healing approach. Very scientific.</p>
    <p class="head">The 8-Laws of Health</p>
    <p class="body">Fundamental to any medical missionary training are the 8 guidelines that help to define and reverse diseases.</p>
  </section>

  <section class="panel panel--pamper">
    <h2 class="title title--boxed">pampering<br>party</h2>
    <p class="head head--u">Massage/Hydrotherapy</p>
    <p class="body" style="margin-top:8px">An introduction to Massage Therapy and Water treatments that help with lowering blood pressure, management of arthritic pain and more.</p>
    <p class="dots" style="margin-top:8px">. . . . . . . . . .</p>
    <p class="head head--u">Cooking Demo</p>
    <p class="body" style="margin-top:8px">This cooking demo is like no other. We know that as a total vegetarian one can enjoy food that is um um good, but just how good? We will invite some of our talented local chefs to lead out in a challenge to see how good is good in the vegetarian world. Meanwhile, you learn how to prepare these meals yourself so that you can go and teach others.</p>
    <p class="slogan">So Fresh and So Clean: It’s God’s will for you to look great.</p>
    <p class="detail"><b>— What can I wear?</b> I’m not a nun but I want to carry myself as an attractive youthful Christian. If you have ever felt anything close to this, you’ll love our class on fashion. We will look at what the bible says on what to wear. You get to attend and participate in our fashion show of classy beautiful looks for the seasons that are easy on the eyes and the pockets. Also learn about natural skin, and hair care. When we are through you’ll be so fresh you would be able to stand yourself.</p>
    <p class="detail"><b>— Time:</b> You set the time.</p>
    <p class="detail"><b>— Location:</b> Your Church.</p>
    <p class="detail"><b>— Cost:</b> $350 covers: course fee and books, DVD’s, additional material.</p>
  </section>

  <section class="panel panel--apply">
    <h2 class="title title--apply">apply<br>here</h2>
    <form class="form" aria-label="Application">
      <h2>Application:</h2>
      <p class="field">Name:<span></span></p>
      <p class="field">Address:<span></span></p>
      <p class="field field--gap">Email:<span></span></p>
      <p class="field">Phone:<span></span></p>
      <p class="field">Church Affiliation:<span></span></p>
      <p class="field">Age:<span></span></p>
    </form>
    <div class="partners">
      <p class="partner"><svg width="10" height="10" viewBox="0 0 10 10"><circle cx="5" cy="5" r="5" fill="var(--sky)"/></svg>Eastbrook</p>
      <p class="partner"><svg width="10" height="10" viewBox="0 0 10 10"><circle cx="5" cy="5" r="5" fill="var(--sky)"/></svg>VelmoraWell</p>
      <p class="partner"><svg width="22" height="22" viewBox="0 0 22 22"><circle cx="11" cy="11" r="11" fill="var(--ink)"/></svg>KR27</p>
    </div>
  </section>

</main>
</body>
</html>
```